Milo Fenwick - Cinematographer

NEED:
I'm looking for a sleek, professional, modern business card that will give give the recipient the impression that they can trust their production will go smoothly by hiring me. I will bring creativity and knowledge to their shoot, so that we can create powerful images.
I am looking for a card with a strong style and design ethos that could be expanded to a website and a full visual/graphic/design entity for me.
ABOUT ME:
I am a mid-twenties cinematographer, I work on music video, narrative short, commercial, and corporate projects. I blend the science and artistry of cameras and filmmaking to tell a story. I'm an artist, a technician, and a manager.
DESIGN:
I like sleek, simple design. Black, dark grays, white, dark navy, steel blues, I love cyan, but also cyan and red. I am not a fan of earthy tones. I generally prefer modern, san-serif fonts over serifs. My old logo was based on an aperture, a multi-blade device at the back of a lens that controls how much light passes through, but I made it with so many colors, that it doesn't necessarily lend itself to a specific color-scheme or design ethos. I liked that the aperture design provided a sense of the technical requirements of my job. I'm a fan of matte business cards, but am open to plenty of specialty print processes to make an outstanding card.
ATTACHED FILES:
My Old Rainbox Aperture Logo, plus a few designs I've tried playing around with, but am not tied to. I AM OPEN TO NEW DESIGNS, DO NOT FEEL TIED TO THIS.
**I've pulled my old logo down from the attached files, and instead attached other business cards I like, so as not to mislead you where I would like to go.
INFO:
Name: Milo Fenwick
Job: Cinematographer
Email: mpfenwick@quellbox.net
Phone: 415.555.0193
Website: milofenwick.net
I'm adding some images of other cards that I like, and removing my old logo, since I'm looking for something new, and don't want that old logo to push anyone a certain direction.

```html
<!DOCTYPE html>
<html lang="en">
<head>
<meta charset="utf-8">
<title>Milo Fenwick – Cinematographer Business Card</title>
<link href="https://fonts.googleapis.com/css2?family=Quicksand:wght@500;600;700&display=swap" rel="stylesheet">
<style>
  :root {
    --stage: #d9d9db;
    --card-dark-top: #3a3a3d;
    --card-dark-bottom: #232325;
    --ink: #0b0b0b;
    --paper: #ffffff;
    --accent-red: #d9262e;
    --mark-ring: #6f7466;
    --mark-core: #141416;
  }
  * { margin: 0; padding: 0; box-sizing: border-box; }
  html, body { width: 1200px; height: 900px; overflow: hidden; }
  body {
    background: var(--stage);
    font-family: "Quicksand", sans-serif;
    position: relative;
  }
  .card {
    position: absolute;
    left: 320px;
    width: 560px;
    height: 320px;
    border-radius: 30px;
    overflow: hidden;
    box-shadow: 0 6px 18px rgba(0,0,0,0.18);
  }

  /* Front */
  .card-front {
    top: 110px;
    background: linear-gradient(160deg, var(--card-dark-top), var(--card-dark-bottom));
  }
  .front-mark {
    position: absolute;
    left: 30px;
    top: 40px;
    width: 240px;
    height: 240px;
    border-radius: 50%;
    background: radial-gradient(circle, var(--mark-core) 55%, #3b3d38 85%, var(--mark-ring) 100%);
  }
  .front-name {
    position: absolute;
    left: 80px;
    top: 118px;
    color: var(--paper);
    font-weight: 700;
    font-size: 62px;
    letter-spacing: 0.5px;
    line-height: 1;
  }
  .front-title {
    position: absolute;
    left: 476px;
    top: 186px;
    color: var(--paper);
    font-weight: 500;
    font-size: 24px;
    line-height: 1;
  }

  /* Back */
  .card-back {
    top: 470px;
    background: var(--paper);
  }
  .name-band {
    position: absolute;
    left: 0;
    top: 38px;
    width: 100%;
    height: 94px;
    background: var(--ink);
  }
  .back-name {
    position: absolute;
    left: 178px;
    top: 44px;
    color: var(--paper);
    font-weight: 700;
    font-size: 38px;
    line-height: 1;
  }
  .back-title {
    position: absolute;
    left: 182px;
    top: 88px;
    color: var(--paper);
    font-weight: 600;
    font-size: 30px;
    line-height: 1;
  }
  .back-mark {
    position: absolute;
    left: 32px;
    top: 112px;
    width: 92px;
    height: 92px;
    border-radius: 50%;
    background: var(--ink);
  }
  .contact {
    position: absolute;
    display: flex;
    align-items: center;
    gap: 10px;
    color: var(--ink);
    font-weight: 500;
    line-height: 1;
  }
  .contact svg { flex: none; }
  .contact-phone { left: 26px; top: 226px; font-size: 22px; }
  .contact-email { left: 276px; top: 210px; font-size: 19px; }
  .contact-web { left: 276px; top: 244px; font-size: 19px; }
  .divider {
    position: absolute;
    left: 258px;
    top: 202px;
    width: 2px;
    height: 72px;
    background: var(--accent-red);
  }
</style>
</head>
<body>

<section class="card card-front" aria-label="Business card front">
  <div class="front-mark"></div>
  <div class="front-name">Milo Fenwick</div>
  <div class="front-title">DP</div>
</section>

<section class="card card-back" aria-label="Business card back">
  <div class="name-band"></div>
  <div class="back-name">Milo Fenwick</div>
  <div class="back-title">Cinematographer</div>
  <div class="back-mark"></div>

  <div class="contact contact-phone">
    <svg width="18" height="18" viewBox="0 0 24 24" aria-hidden="true">
      <path fill="#0b0b0b" d="M6.6 10.8c1.4 2.8 3.8 5.1 6.6 6.6l2.2-2.2c.3-.3.7-.4 1-.2 1.1.4 2.3.6 3.6.6.6 0 1 .4 1 1V20c0 .6-.4 1-1 1C10.6 21 3 13.4 3 4c0-.6.4-1 1-1h3.5c.6 0 1 .4 1 1 0 1.2.2 2.4.6 3.6.1.3 0 .7-.2 1l-2.3 2.2z"/>
    </svg>
    <span>415.555.0193</span>
  </div>

  <div class="divider"></div>

  <div class="contact contact-email">
    <svg width="24" height="18" viewBox="0 0 24 18" aria-hidden="true">
      <rect x="0" y="0" width="24" height="18" rx="1.5" fill="#0b0b0b"/>
      <path d="M2 2l10 8 10-8" fill="none" stroke="#fff" stroke-width="1.6"/>
    </svg>
    <span>mpfenwick@quellbox.net</span>
  </div>

  <div class="contact contact-web">
    <svg width="22" height="22" viewBox="0 0 24 24" aria-hidden="true">
      <circle cx="12" cy="12" r="10.5" fill="none" stroke="#0b0b0b" stroke-width="2"/>
      <ellipse cx="12" cy="12" rx="4.5" ry="10.5" fill="none" stroke="#0b0b0b" stroke-width="1.6"/>
      <path d="M1.5 12h21M3.5 6.5h17M3.5 17.5h17" stroke="#0b0b0b" stroke-width="1.6"/>
    </svg>
    <span>www.milofenwick.net</span>
  </div>
</section>

</body>
</html>
```